Personality Workshop Template

I teach a workshop to business people that helps them identify and work with different personality types. We recently had our workbook redesigned and I want the power point to match. (This designer doesn't do power points.) I will upload both the workbook and the current class. I need a matching look that I can use for future classes. Each class is tailored to the client. I need 3-4 template slides that I can use interchangeably as I tailor the classes.

```html
<!DOCTYPE html>
<html lang="en">
<head>
<meta charset="utf-8">
<title>Workshop Slide Template</title>
<link rel="stylesheet" href="https://fonts.googleapis.com/css2?family=Roboto+Condensed:wght@400;500;700&display=swap">
<style>
  :root {
    --blue-core: #2c5cc4;
    --blue-mid: #234ead;
    --blue-edge: #183b8e;
    --blue-footer: #1c469c;
    --green: #8cd628;
    --white: #ffffff;
  }
  * { margin: 0; padding: 0; box-sizing: border-box; }
  html, body { width: 1200px; height: 900px; overflow: hidden; background: var(--blue-edge); }
  .slide {
    position: relative;
    width: 1200px;
    height: 900px;
    overflow: hidden;
    font-family: "Roboto Condensed", "Arial Narrow", sans-serif;
    color: var(--white);
    background:
      radial-gradient(ellipse 70% 60% at 55% 45%, var(--blue-core) 0%, var(--blue-mid) 55%, var(--blue-edge) 100%);
  }
  .bullet-list { list-style: none; position: absolute; left: 0; top: 0; width: 100%; }
  .bullet-item {
    position: absolute;
    left: 34px;
    display: flex;
    align-items: center;
    gap: 26px;
    font-size: 28px;
    font-weight: 500;
    letter-spacing: 1px;
    white-space: nowrap;
    transform: translateY(-50%);
  }
  .bullet-icon { width: 40px; height: 40px; flex: none; }
  .footer-wave { position: absolute; left: 0; top: 0; width: 1200px; height: 900px; }
  .program-name {
    position: absolute;
    left: 12px;
    top: 848px;
    font-size: 34px;
    font-weight: 700;
    letter-spacing: 0.5px;
  }
  .copyright {
    position: absolute;
    left: 648px;
    top: 850px;
    font-size: 18px;
    font-weight: 700;
  }
  .company {
    position: absolute;
    right: 30px;
    top: 808px;
    display: flex;
    align-items: center;
    gap: 12px;
    font-size: 26px;
    font-weight: 700;
    line-height: 1.05;
  }
  .company-dot { width: 22px; height: 22px; border-radius: 50%; background: var(--white); flex: none; }
</style>
</head>
<body>
<div class="slide">
  <ul class="bullet-list">
    <li class="bullet-item" style="top:92px">
      <svg class="bullet-icon" viewBox="0 0 40 40"><circle cx="20" cy="20" r="18" fill="#1a3f96" stroke="#ffffff" stroke-width="2"/><path d="M16 12 L24 20 L16 28" fill="none" stroke="#8cd628" stroke-width="4.5"/></svg>
      <span>Lorem ipsum dolor sit lorem ipsum dolor sit&nbsp; Lorem ipsum dolor sit lorem</span>
    </li>
    <li class="bullet-item" style="top:180px">
      <svg class="bullet-icon" viewBox="0 0 40 40"><circle cx="20" cy="20" r="18" fill="#1a3f96" stroke="#ffffff" stroke-width="2"/><path d="M16 12 L24 20 L16 28" fill="none" stroke="#8cd628" stroke-width="4.5"/></svg>
      <span>Lorem ipsum dolor sit lorem ipsum dolor sit&nbsp; Lorem ipsum dolor sit lorem</span>
    </li>
    <li class="bullet-item" style="top:271px">
      <svg class="bullet-icon" viewBox="0 0 40 40"><circle cx="20" cy="20" r="18" fill="#1a3f96" stroke="#ffffff" stroke-width="2"/><path d="M16 12 L24 20 L16 28" fill="none" stroke="#8cd628" stroke-width="4.5"/></svg>
      <span>Lorem ipsum dolor sit lorem ipsum dolor sit&nbsp; Lorem ipsum dolor sit lorem</span>
    </li>
    <li class="bullet-item" style="top:366px">
      <svg class="bullet-icon" viewBox="0 0 40 40"><circle cx="20" cy="20" r="18" fill="#1a3f96" stroke="#ffffff" stroke-width="2"/><path d="M16 12 L24 20 L16 28" fill="none" stroke="#8cd628" stroke-width="4.5"/></svg>
      <span>Lorem ipsum dolor sit lorem ipsum dolor sit&nbsp; Lorem ipsum dolor sit lorem</span>
    </li>
    <li class="bullet-item" style="top:462px">
      <svg class="bullet-icon" viewBox="0 0 40 40"><circle cx="20" cy="20" r="18" fill="#1a3f96" stroke="#ffffff" stroke-width="2"/><path d="M16 12 L24 20 L16 28" fill="none" stroke="#8cd628" stroke-width="4.5"/></svg>
      <span>Lorem ipsum dolor sit lorem ipsum dolor sit&nbsp; Lorem ipsum dolor sit lorem</span>
    </li>
    <li class="bullet-item" style="top:573px">
      <svg class="bullet-icon" viewBox="0 0 40 40"><circle cx="20" cy="20" r="18" fill="#1a3f96" stroke="#ffffff" stroke-width="2"/><path d="M16 12 L24 20 L16 28" fill="none" stroke="#8cd628" stroke-width="4.5"/></svg>
      <span>Lorem ipsum dolor sit lorem ipsum dolor sit&nbsp; Lorem ipsum dolor sit lorem</span>
    </li>
  </ul>

  <svg class="footer-wave" viewBox="0 0 1200 900" aria-hidden="true">
    <path d="M0 778 C110 830 300 818 600 768 C850 726 1050 706 1200 745 L1200 900 L0 900 Z" fill="#1c469c"/>
    <path d="M0 778 C110 830 300 818 600 768 C850 726 1050 706 1200 745" fill="none" stroke="#8cd628" stroke-width="5"/>
  </svg>

  <div class="program-name">PEOPLE WORKSHOP</div>
  <div class="copyright">Copyright text here</div>
  <div class="company">
    <span class="company-dot"></span>
    <span>Brio Business<br>Consulting</span>
  </div>
</div>
</body>
</html>
```